Creative, fresh business card design for Orrin Linings

We need a fresh, creative business card design for Orrin Linings. We are the manufacturer of Orrin Linings in Australia. Wall panels are 2400 x 1200mm panels made from MDF and feature 3D patterns on the face of the panel. The colours to be used are green, silver/grey and white RGB
Red 187
Green 207
Blue 65.

An idea is to possibly use a watermark of one of our designs as a background (like on the "Ferns" design on the left hand side of page 2 of our brochure).

Target Market(s)

Interior designers, architects, builders and home renovators

Industry/Entity Type

Business

Contact Information for Business Card

Details to go on the card are:
Our logo (attached),
Slogan: "Decorative panels for interiors and exteriors",
Contact name,
Position,
Mobile phone number,
Business address,
Business phone,
Business fax,
Website and
Email address.

I have attached a few images of our panels and our brochure for reference.

The colours of the business card should feature our logo colours which are: RGB
Red 187
Green 207
Blue 65

Requirements
Must have
• Very modern fonts and design. Some of the designs shown especially the "Weave" design which is a popular design.
Nice to have
• Creative but simple design. Very contemporary.
Should not have
• Anything ornate or old fashioned.

```html
<!DOCTYPE html>
<html lang="en">
<head>
<meta charset="utf-8">
<title>Orrin Linings – Business Card</title>
<link href="https://fonts.googleapis.com/css2?family=Arimo:wght@400;700&display=swap" rel="stylesheet">
<style>
  :root {
    --backdrop: #231f20;
    --card: #ffffff;
    --lime: #bbcf41;
    --lime-bright: #c2d82e;
    --ink: #1d1d1b;
    --grey: #8a8a8d;
    --panel-dark: #3e3e40;
    --panel-mid: #8d8d8f;
    --panel-light: #c9c9c9;
  }
  * { margin: 0; padding: 0; box-sizing: border-box; }
  html, body {
    width: 1200px; height: 853px; overflow: hidden;
    background: var(--backdrop);
    font-family: "Arimo", Arial, sans-serif;
  }
  .card {
    position: absolute; left: 165px; top: 191px;
    width: 853px; height: 510px;
    background: var(--card); overflow: visible;
  }
  .panel-photo {
    position: absolute; left: 0; top: 0; width: 853px; height: 510px;
  }
  .brand {
    position: absolute; left: 37px; top: 62px;
    display: flex; align-items: center; gap: 16px;
  }
  .brand-square { width: 58px; height: 58px; background: var(--lime-bright); }
  .brand-name {
    font-size: 40px; font-weight: 700; color: var(--grey);
    letter-spacing: -0.5px; line-height: 1;
  }
  .slogan {
    position: absolute; left: 437px; top: 67px;
    width: 418px; height: 95px;
    background: var(--lime-bright); color: #fff;
    font-size: 28.5px; line-height: 34px;
    padding: 15px 0 0 43px; letter-spacing: 0.3px;
  }
  .person-name {
    position: absolute; left: 35px; top: 246px;
    font-size: 24px; font-weight: 700; color: var(--lime-bright);
    letter-spacing: 0.3px;
  }
  .person-role {
    position: absolute; left: 35px; top: 279px;
    font-size: 17px; color: #3a3a3a;
  }
  .contact {
    position: absolute; display: flex; align-items: center;
    font-size: 19px; color: var(--ink); white-space: nowrap;
  }
  .contact svg { flex: none; }
  .contact .icon { position: absolute; }
  .contact-mobile { left: 64px; top: 322px; font-weight: 700; }
  .contact-phone { left: 64px; top: 357px; }
  .contact-fax { left: 241px; top: 357px; }
  .contact-email { left: 64px; top: 396px; font-size: 18.5px; }
  .contact-web { left: 64px; top: 430px; font-size: 23px; font-weight: 700; }
  .contact-address { left: 64px; top: 467px; font-size: 19px; }
  .icon { stroke: var(--lime-bright); fill: none; stroke-width: 1.6; }
</style>
</head>
<body>
  <div class="card">
    <svg class="panel-photo" viewBox="0 0 853 510" role="img" aria-label="Photograph of a dark grey wavy 3D wall panel beside a bright dining room with glass doors">
      <defs>
        <linearGradient id="panelTone" x1="0" y1="0" x2="1" y2="0.4">
          <stop offset="0" stop-color="#4a4a4c"/>
          <stop offset="0.55" stop-color="#6e6e70"/>
          <stop offset="0.8" stop-color="#9a9a9a"/>
          <stop offset="1" stop-color="#c7c9c6"/>
        </linearGradient>
      </defs>
      <polygon points="461,0 853,0 853,506 461,414" fill="url(#panelTone)"/>
    </svg>

    <div class="brand">
      <span class="brand-square"></span>
      <span class="brand-name">Orrin Linings</span>
    </div>

    <div class="slogan">Decorative panels for<br>interior &amp; landscapes</div>

    <div class="person-name">MARA LINDQVIST</div>
    <div class="person-role">Owner,</div>

    <div class="contact contact-mobile" style="transform:translateY(-50%)">
      <svg class="icon" style="left:-33px" width="16" height="26" viewBox="0 0 16 26"><rect x="1" y="1" width="14" height="24" rx="2"/><line x1="1" y1="20" x2="15" y2="20"/></svg>
      00 987 654 321
    </div>
    <div class="contact contact-phone" style="transform:translateY(-50%)">
      <svg class="icon" style="left:-35px" width="28" height="20" viewBox="0 0 28 20"><path d="M2 8 Q14 -1 26 8 L22 10 L19 6 Q14 4 9 6 L6 10 Z"/><path d="M7 10 L5 18 H23 L21 10"/><circle cx="14" cy="14" r="2.5"/></svg>
      02 5550 1842
    </div>
    <div class="contact contact-fax" style="transform:translateY(-50%)">
      <svg class="icon" style="left:-36px" width="28" height="26" viewBox="0 0 28 26"><rect x="1" y="4" width="7" height="21" rx="2"/><rect x="8" y="8" width="18" height="17" rx="1"/><rect x="12" y="1" width="10" height="7"/><line x1="12" y1="13" x2="22" y2="13"/><line x1="12" y1="17" x2="22" y2="17"/><line x1="12" y1="21" x2="22" y2="21"/></svg>
      02 5550 1843
    </div>
    <div class="contact contact-email" style="transform:translateY(-50%)">
      <svg class="icon" style="left:-34px" width="24" height="24" viewBox="0 0 24 24"><circle cx="12" cy="12" r="4.5"/><path d="M16.5 8 V14 Q16.5 17 19 17 Q22.5 17 22.5 12 A10.5 10.5 0 1 0 17 21"/></svg>
      sales@orrinlinings.com.au
    </div>
    <div class="contact contact-web" style="transform:translateY(-50%)">www.orrinlinings.com.au</div>
    <div class="contact contact-address" style="transform:translateY(-50%)">
      <svg class="icon" style="left:-34px" width="22" height="28" viewBox="0 0 22 28"><path d="M11 27 C4 18 1 14 1 10 A10 10 0 0 1 21 10 C21 14 18 18 11 27 Z"/><circle cx="11" cy="10" r="4"/></svg>
      14 Callow Street, Brookvale NSW 2100
    </div>
  </div>
</body>
</html>
```